Larkmoor Business Card Design Project

Double side card , just the logo on oxford white background on one side , and the rest of the information on the other side..
the company name is : Larkmoor Continental General Trading LLC.
logo is already attached
the card to show in the info side: company name, employee name and position (job title) phone number, fax number, email address, P.O. box, Location (city and country)
deadline is already extended 4 all to have more time... thanks

```html
<!DOCTYPE html>
<html lang="en">
<head>
<meta charset="utf-8">
<title>Larkmoor Business Card</title>
<link rel="stylesheet" href="https://fonts.googleapis.com/css2?family=Lato:wght@400;700;900&display=swap">
<style>
  :root {
    --backdrop: #8c8c8c;
    --card-dark: #3c3d3f;
    --card-white: #ffffff;
    --oxford-white: #f4f3ee;
    --text-light: #e8e8e8;
    --text-white: #ffffff;
    --accent-cyan: #1ba9d6;
    --tile-cyan: #19b3dc;
    --tile-mid: #1a8fcb;
    --tile-deep: #1660a8;
    --logo-ink: #3a3b3d;
    --muted-ink: #6b6c6f;
    --divider: rgba(255,255,255,0.12);
  }
  * { box-sizing: border-box; margin: 0; padding: 0; }
  html, body { width: 1200px; height: 910px; overflow: hidden; }
  body {
    background: var(--backdrop);
    font-family: "Lato", Arial, sans-serif;
    position: relative;
  }
  .card {
    position: absolute;
    left: 250px;
    width: 700px;
    height: 400px;
    overflow: hidden;
    box-shadow: 0 6px 18px rgba(0,0,0,0.25);
  }
  /* Logo side */
  .card--logo {
    top: 35px;
    background: var(--oxford-white);
    display: flex;
    align-items: center;
    justify-content: center;
  }
  .card--logo .brand-name {
    color: var(--logo-ink);
    font-size: 52px;
    font-weight: 700;
    letter-spacing: 2px;
  }
  /* Info side */
  .card--info { top: 475px; background: var(--card-dark); }
  .card--info .shapes { position: absolute; inset: 0; }
  .person { position: absolute; left: 50px; top: 68px; }
  .person__name {
    color: var(--text-white);
    font-weight: 900;
    font-size: 21px;
    letter-spacing: 0.5px;
    text-transform: uppercase;
  }
  .person__title {
    color: var(--accent-cyan);
    font-size: 16px;
    margin-top: 3px;
  }
  .contact {
    position: absolute;
    left: 50px;
    width: 310px;
    color: var(--text-light);
    font-size: 16.5px;
    line-height: 24px;
  }
  .contact--address { top: 153px; }
  .contact--phone { top: 209px; }
  .contact--web { top: 265px; }
  .divider {
    position: absolute;
    left: 50px;
    width: 310px;
    height: 1px;
    background: var(--divider);
  }
  .divider--one { top: 204px; }
  .divider--two { top: 260px; }
  .company {
    position: absolute;
    left: 478px;
    top: 172px;
    width: 205px;
  }
  .company .brand-name {
    display: block;
    color: var(--logo-ink);
    font-size: 30px;
    font-weight: 700;
    letter-spacing: 1px;
  }
  .company__legal {
    color: var(--muted-ink);
    font-size: 11px;
    line-height: 15px;
    margin-top: 6px;
    letter-spacing: 0.3px;
  }
</style>
</head>
<body>

<section class="card card--logo">
  <span class="brand-name">Larkmoor Int.</span>
</section>

<section class="card card--info">
  <svg class="shapes" width="700" height="400" viewBox="0 0 700 400">
    <polygon class="panel-white" points="370,0 700,0 700,400 520,400" fill="var(--card-white)"/>
    <rect class="tile tile--home" x="368" y="150" width="56" height="56" fill="var(--tile-cyan)"/>
    <rect class="tile tile--phone" x="368" y="206" width="56" height="56" fill="var(--tile-mid)"/>
    <rect class="tile tile--web" x="368" y="262" width="56" height="56" fill="var(--tile-deep)"/>
    <g class="icon icon--home" fill="#fff">
      <polygon points="386,179 396,170 406,179"/>
      <rect x="389" y="179" width="14" height="9"/>
    </g>
    <g class="icon icon--phone" fill="#fff">
      <path d="M385,231 Q396,223 407,231 L405,235 L401,234 L400,231 Q396,229 392,231 L391,234 L387,235 Z"/>
      <rect x="389" y="234" width="14" height="9" rx="1.5"/>
    </g>
    <g class="icon icon--web" fill="none" stroke="#fff" stroke-width="2.2">
      <rect x="386" y="280" width="20" height="14"/>
      <line x1="396" y1="294" x2="396" y2="299"/>
      <line x1="390" y1="299" x2="402" y2="299"/>
    </g>
  </svg>

  <div class="person">
    <div class="person__name">Dara K. Whitfield</div>
    <div class="person__title">CEO</div>
  </div>

  <div class="contact contact--address">P.O. Box 4417<br>Marlow, Oregon, USA</div>
  <div class="divider divider--one"></div>
  <div class="contact contact--phone">(555) 318-2046<br>F: (555) 318-2047</div>
  <div class="divider divider--two"></div>
  <div class="contact contact--web">DaraKWhitfield@corvanta.com<br>www.corvanta.com</div>

  <div class="company">
    <span class="brand-name">Larkmoor Int.</span>
    <div class="company__legal">Larkmoor Continental General Trading LLC.</div>
  </div>
</section>

</body>
</html>
```